Bright Towns Alliance PowerPoint Design Template and Sample Deck

The Bright Towns Alliance is an international organization that seeks to improve the livability, workability and sustainability of the world’s cities.
We seek a versatile PowerPoint design template with 10 slide types plus a “self-documenting” sample deck. Your design will be used in keynote speeches and workshops around the world.
After the contest is completed, we will ask the winning designer to add 10-20 additional slide types for $75 per slide. We also seek a long-term relationship whereby we can request “custom” slides and/or ask the designer to touch up the slides we build to make them better.
FILES. We have uploaded several files:
2. PALETTE. Shows our official colors.
3 LOGOS. Several individual files with different variations of our logo. Some with our motto, some without.
2. SAMPLE SLIDES. Because we were unable to successfully upload our sample deck, we are making it available via this FileCrate link:
https://www.filecrate-example.net/s/q7mrk2tzw9hdn4e/The%20Bright%20Towns%20Alliance%20Design%20Contest%20Notes.docx?dl=0
Target Market(s)
Mayors, department heads, CIOs, senior executives from technology companies
Industry/Entity Type
Information Technology
Colors
Designer to choose colors to be used in the design.
Requirements
Must have
- Please see uploaded Word document for requirements, nice to haves and should not haves and uploaded palette for color preferences.
Nice to have
- see above
Should not have
- see above

```html
<!DOCTYPE html>
<html lang="en">
<head>
<meta charset="utf-8">
<title>Bright Towns Alliance – Template Overview</title>
<link href="https://fonts.googleapis.com/css2?family=Open+Sans:wght@400;600;700&display=swap" rel="stylesheet">
<style>
:root{
  --navy:#0d2a55;
  --navy-2:#1c3f74;
  --sky:#6f9bd6;
  --sky-2:#8fb2e2;
  --orange:#f58220;
  --ink:#333;
  --muted:#8a8a8a;
  --line:#d6d6d6;
  --canvas:#d9dadc;
  --green:#8cc63f;
  --red:#f15a29;
  --purple:#7e57b2;
}
*{box-sizing:border-box;margin:0;padding:0}
html,body{width:1200px;height:914px;overflow:hidden;background:var(--canvas);font-family:"Open Sans",Arial,sans-serif;color:var(--ink)}
.board{position:relative;width:1200px;height:914px}
.slide{position:absolute;width:392px;height:220px;overflow:hidden;background:#fff}
.c1{left:7px}.c2{left:404px}.c3{left:802px}
.r1{top:6px}.r2{top:232px}.r3{top:458px}.r4{top:685px}
.abs{position:absolute}
.stripe{position:absolute;left:0;top:0;bottom:0;width:12px;background:var(--navy)}
.stripe::after{content:"";position:absolute;left:12px;top:0;bottom:0;width:5px;background:var(--sky)}
.title{position:absolute;left:28px;top:12px;font-size:11px;color:#222;text-transform:uppercase;letter-spacing:.2px}
.title em{font-style:normal;color:var(--orange)}
.title.light{color:#fff}
.brand{position:absolute;top:10px;right:32px;font-size:6.4px;font-weight:600;color:var(--navy);white-space:nowrap}
.pageno{position:absolute;top:7px;right:0;width:26px;height:15px;background:var(--navy);color:#fff;font-size:5px;font-weight:700;display:flex;align-items:center;justify-content:center}
.photo{position:absolute}
.tiny{font-size:5px;line-height:1.45;color:var(--muted)}
.btn{position:absolute;background:var(--orange);color:#fff;font-size:5.5px;font-weight:700;border-radius:8px;display:flex;align-items:center;justify-content:center}

/* cover */
.cover-photo{left:0;top:0;width:392px;height:168px;background:linear-gradient(180deg,#5d6670 0%,#8d96a0 45%,#4e5761 62%,#7c8691 100%)}
.cover-band{left:0;top:168px;width:392px;height:43px;background:#fff}
.cover-foot{left:0;top:211px;width:392px;height:9px;background:#1d1f24}
.cover-title{right:70px;top:173px;font-size:15px;color:var(--navy);font-weight:700;white-space:nowrap}
.cover-title span{font-weight:400}
.cover-sub{right:62px;top:194px;font-size:6.5px;color:var(--orange);letter-spacing:.3px}
.cover-rule{left:344px;top:174px;width:1px;height:30px;background:#bbb}
.cover-logo{left:350px;top:175px;font-size:8px;line-height:1.05;color:var(--navy)}
.contact{right:32px;text-align:right;font-size:4.6px;color:#fff;line-height:1.3}
.contact-ico{right:26px;width:7px;height:7px}

/* agenda */
.agenda-photo{left:0;top:0;width:182px;height:220px;background:linear-gradient(160deg,#9fb3cc 0%,#6f8fb8 50%,#4c6f9f 100%)}
.agenda-col{left:182px;top:0;width:12px;height:220px;background:#c9d5e6}
.chap{font-size:5.3px;font-weight:700;color:#fff}
.chap-line{height:1px;background:rgba(255,255,255,.8)}
.agenda-num{left:165px;font-size:5px;color:#fff}
.agenda-row{left:192px;width:180px;font-size:5px;color:#666;display:flex;justify-content:space-between}
.agenda-row.hl{color:var(--orange);font-weight:700}
.agenda-row.hl::after{content:"";position:absolute;left:0;right:28px;bottom:-3px;height:1px;background:#888}

/* banner */
.banner-photo{left:0;top:0;width:392px;height:220px;background:linear-gradient(100deg,#3d4e63 0%,#5c6f85 45%,#8092a6 70%,#3a4a5e 100%)}
.banner-panel{left:28px;top:0;width:170px;height:220px;background:rgba(30,55,95,.55)}
.banner-title{left:42px;top:76px;font-size:10px;color:#fff;font-weight:600}
.banner-title em{font-style:normal;color:var(--orange)}
.banner-text{left:42px;top:100px;width:118px;font-size:6.6px;line-height:1.4;color:#dde6f2;text-align:justify}
.banner-text b{color:#fff}

/* quote */
.quote-photo{left:0;top:0;width:392px;height:220px;background:linear-gradient(90deg,#1f3c66 0%,#2f4f7d 40%,#7b8ea7 70%,#c9cdd2 100%)}
.quote-text{left:40px;top:72px;width:140px;text-align:center;font-size:6.6px;line-height:1.55;color:#c9d6ea}
.quote-text b{color:#fff}

/* text heavy */
.th-photo{left:200px;top:0;width:192px;height:220px;background:linear-gradient(120deg,rgba(255,255,255,1) 0%,#eef1f5 40%,#dfe5ec 100%)}
.th-intro{left:28px;top:46px;width:170px;font-size:5.8px;line-height:1.35;color:#777}
.th-list{left:28px;top:84px;list-style:none}
.th-list li{font-size:5.2px;color:#666;margin-bottom:8px;display:flex;gap:6px;align-items:center}
.th-box{left:28px;top:158px;width:160px;height:34px;background:var(--orange);color:#fff;font-size:5.6px;font-weight:600;line-height:1.4;padding:5px 8px}
.th-box b{color:var(--navy)}

/* stats */
.st-photo{left:0;top:0;width:392px;height:163px;background:linear-gradient(180deg,#f4f6f8 0%,#e9edf1 100%)}
.stat{top:60px;width:90px;text-align:center}
.stat-num{font-size:12.5px;font-weight:700;color:var(--navy);margin-top:6px}
.stat-lab{font-size:5.6px;color:var(--orange);margin-top:9px}
.stat-sep{top:78px;width:1px;height:36px;background:#c8ccd2}
.st-band{left:0;top:163px;width:392px;height:57px;background:var(--navy)}
.st-head{left:20px;top:170px;font-size:8.6px;font-weight:700;color:#fff}
.st-text{left:20px;top:184px;width:210px;font-size:5.2px;line-height:1.5;color:#b9c7dd}
.url-pill{left:250px;top:183px;width:116px;height:12px;background:#fff;border-radius:6px;font-size:4.8px;color:var(--navy);font-weight:600;display:flex;align-items:center;padding-left:22px}
.url-pill::before{content:"";position:absolute;left:0;top:0;width:18px;height:12px;background:var(--orange);border-radius:6px 0 0 6px}

/* world map */
.map{left:26px;top:50px;width:218px;height:130px;background:linear-gradient(90deg,#7ea3d4 0%,#7ea3d4 30%,#f7b57a 45%,#bcbcbc 65%,#c6c6c6 100%);border-radius:40px 60px 50px 70px;opacity:.9}
.map-rule{left:250px;top:38px;width:1px;height:150px;border-left:1px dotted #bbb}
.region{width:60px}
.region .pct{font-size:11px;color:var(--orange)}
.region .name{font-size:6.6px;font-weight:700;color:var(--navy);margin-top:2px}
.region .desc{font-size:4.8px;color:#888;line-height:1.4;margin-top:3px}

/* table */
.tb-ico{width:30px;height:30px}
.tb-head{left:124px;top:63px;font-size:5.6px;color:var(--orange);font-weight:600}
.tb-lead{left:124px;top:73px;width:160px;font-size:4.6px;line-height:1.35;color:#999;font-style:italic}
.grid{left:36px;top:105px;width:282px;font-size:4.6px;color:#888;border-collapse:collapse}
.grid th{color:var(--orange);font-size:5.6px;font-weight:700;text-align:left;padding:2px 0 3px;border-bottom:1px solid #888}
.grid td{padding:2.6px 0;border-bottom:1px solid #e2e2e2}
.grid tfoot td{color:var(--orange);font-weight:700;font-size:5.4px;border-bottom:none;padding-top:5px}
.mgr{left:290px;top:62px;width:86px}
.mgr-head{background:var(--navy);color:#fff;font-size:5.2px;font-weight:700;padding:5px 10px}
.mgr-cell{background:var(--sky);color:#fff;font-size:4.8px;padding:5px 18px;border-top:1px solid #fff;height:27px;line-height:1.45}
.mgr-cell b{display:block;font-size:5.4px}

/* two pictures */
.tp-left{left:24px;top:56px;width:128px;height:82px;background:linear-gradient(180deg,#b8c2cc 0%,#c9a57d 55%,#6b6052 100%)}
.tp-mid{left:152px;top:56px;width:114px;height:82px;background:var(--navy)}
.tp-right{left:266px;top:56px;width:126px;height:82px;background:linear-gradient(180deg,#9db5cf 0%,#c3ad8d 55%,#5b5a5c 100%)}
.tp-head{left:152px;top:66px;width:114px;text-align:center;font-size:8.8px;font-weight:700;color:#fff}
.tp-text{left:162px;top:82px;width:96px;text-align:center;font-size:4.6px;line-height:1.35;color:#dbe3ef}
.tp-body{left:52px;top:158px;width:318px;text-align:center;font-size:5.2px;line-height:2.2;color:#999}

/* timeline */
.tl-text{font-size:4.8px;line-height:1.35;color:#888;width:58px}
.tl-text b{color:#444;font-weight:600}
.tl-month{font-size:4.8px;color:var(--sky)}
.tl-year{font-size:5px;font-weight:700;color:#444}

/* process */
.pr-note{font-size:4.8px;line-height:1.35;color:#555;width:60px}

/* thank you */
.ty-photo{left:0;top:0;width:392px;height:220px;background:linear-gradient(180deg,#2a4263 0%,#3f5878 40%,#223a5a 100%)}
.ty-head{left:0;width:392px;top:70px;text-align:center;font-size:15px;font-weight:700;color:#fff}
.ty-head em{font-style:normal;color:var(--orange)}
.ty-text{left:110px;top:96px;width:190px;text-align:center;font-size:5px;line-height:1.45;color:#c6d2e2}
.ty-contact{top:128px;text-align:center;font-size:4px;color:#fff;width:60px}
.ty-pill{left:165px;top:160px;width:90px;height:11px;background:#fff;border-radius:6px;font-size:5px;font-weight:600;color:var(--navy);display:flex;align-items:center;justify-content:center}
</style>
</head>
<body>
<div class="board">

<!-- 1 cover -->
<section class="slide c1 r1">
  <div class="photo abs cover-photo" role="img" aria-label="City skyline across the water under a grey sky"></div>
  <div class="abs contact" style="top:8px">+1 555 0148</div>
  <div class="abs contact" style="top:20px">hello@brighttowns-example.org</div>
  <div class="abs contact" style="top:32px">3rd floor Harbor House,<br>Lakeport</div>
  <svg class="abs contact-ico" style="top:7px" viewBox="0 0 10 10"><path d="M2 1l2 2-1 1.5c.8 1.5 1.8 2.5 3 3L7.5 6l2 2-1.5 1.5C4 9 1 6 .5 2.5z" fill="var(--orange)"/></svg>
  <svg class="abs contact-ico" style="top:20px" viewBox="0 0 10 10"><rect x="1" y="2" width="8" height="6" fill="var(--orange)"/><path d="M1 2l4 3.5L9 2" stroke="#fff" stroke-width=".8" fill="none"/></svg>
  <svg class="abs contact-ico" style="top:33px" viewBox="0 0 10 10"><path d="M5 9.5S1.5 5.8 1.5 3.6a3.5 3.5 0 017 0C8.5 5.8 5 9.5 5 9.5z" fill="var(--orange)"/><circle cx="5" cy="3.6" r="1.2" fill="#fff"/></svg>
  <div class="abs cover-band"></div>
  <div class="abs cover-title">2018 BrightTowns <span>Integration</span></div>
  <div class="abs cover-sub">INTEGRATION REPORT</div>
  <div class="abs cover-rule"></div>
  <div class="abs cover-logo">Bright<br>Towns<br>Alliance</div>
  <div class="abs cover-foot"></div>
</section>

<!-- 2 agenda -->
<section class="slide c2 r1">
  <div class="photo abs agenda-photo" role="img" aria-label="Presenter at a whiteboard with a seated colleague, blue tint"></div>
  <div class="abs agenda-col"></div>
  <div class="stripe" style="width:6px"></div>
  <div class="title light">Progressive <em>Agenda</em></div>
  <div class="brand">Bright Towns Alliance</div>
  <div class="pageno">2</div>
  <div class="abs chap" style="left:118px;top:60px">CHAPTER I</div>
  <div class="abs chap-line" style="left:110px;top:71px;width:55px"></div>
  <div class="abs chap" style="left:118px;top:122px">CHAPTER II</div>
  <div class="abs chap-line" style="left:110px;top:133px;width:55px"></div>
  <div class="abs agenda-num" style="top:77px">02</div>
  <div class="abs agenda-num" style="top:93px">03</div>
  <div class="abs agenda-num" style="top:109px">04</div>
  <div class="abs agenda-num" style="top:141px">06</div>
  <div class="abs agenda-num" style="top:157px">07</div>
  <div class="abs agenda-num" style="top:173px">08</div>
  <div class="abs agenda-row hl" style="top:61px"><span>SELF-AWARENESS</span><span>01</span></div>
  <div class="abs agenda-row" style="top:77px"><span>Professional Integrity</span><span>02</span></div>
  <div class="abs agenda-row" style="top:93px"><span>Leadership In The Entry Level</span><span>03</span></div>
  <div class="abs agenda-row" style="top:109px"><span>Trust, Accountability &amp; Reliability</span><span>04</span></div>
  <div class="abs agenda-row hl" style="top:125px"><span>THE VALUE OF QUESTIONS</span><span>05</span></div>
  <div class="abs agenda-row" style="top:141px"><span>Owning Mistakes</span><span>06</span></div>
  <div class="abs agenda-row" style="top:157px"><span>Resilience In The Face of Challenges</span><span>07</span></div>
  <div class="abs agenda-row" style="top:173px"><span>Utilizing Your Strengths</span><span>08</span></div>
</section>

<!-- 3 picture banner -->
<section class="slide c3 r1">
  <div class="photo abs banner-photo" role="img" aria-label="Aerial view of downtown towers at dusk"></div>
  <div class="abs banner-panel"></div>
  <div class="brand" style="color:#fff">Bright Towns Alliance</div>
  <div class="pageno">3</div>
  <div class="abs banner-title">PICTURE <em>BANNER</em></div>
  <p class="abs banner-text"><b>Cras at malesuada ipsum.</b> Ut vestibulum, erat quis dictum consequat, eros ante bibendum nisl, non interdum erat tortor et odio.</p>
  <div class="btn" style="left:44px;top:174px;width:82px;height:11px">Visit Us</div>
  <svg class="abs" style="left:46px;top:175px;width:9px;height:9px" viewBox="0 0 10 10"><circle cx="5" cy="5" r="4" fill="none" stroke="#fff" stroke-width=".8"/><path d="M1 5h8M5 1c-2 2.5-2 5.5 0 8M5 1c2 2.5 2 5.5 0 8" stroke="#fff" stroke-width=".6" fill="none"/></svg>
</section>

<!-- 4 picture quotation -->
<section class="slide c1 r2">
  <div class="photo abs quote-photo" role="img" aria-label="Smiling businessman in a suit gesturing to the side"></div>
  <div class="stripe"></div>
  <div class="title light">Picture <em>Quotation</em></div>
  <div class="brand">Bright Towns Alliance</div>
  <div class="pageno">4</div>
  <svg class="abs" style="left:98px;top:40px;width:26px;height:22px" viewBox="0 0 26 22"><path d="M13 2c6 0 11 3.5 11 8s-5 8-11 8c-1.5 0-3-.2-4.2-.6L3 20l2-4.5C3 14 2 12 2 10c0-4.5 5-8 11-8z" fill="none" stroke="#fff" stroke-width="1.2"/></svg>
  <p class="abs quote-text"><b>Cras at malesuada ipsum.</b> Ut vestibulum, erat quis dictum consequat, eros ante bibendum nisl, non interdum erat tortor et odio. Morbi libero nulla, convallis et quam et, condimentum fringilla ligula.</p>
  <div class="btn" style="left:68px;top:165px;width:78px;height:14px;font-size:6.5px">ALEX MORAN, CEO</div>
</section>

<!-- 5 text heavy -->
<section class="slide c2 r2">
  <div class="photo abs th-photo" role="img" aria-label="Hands typing on a laptop beside printed charts, faded"></div>
  <div class="stripe"></div>
  <div class="title">Text <em>Heavy</em></div>
  <div class="brand">Bright Towns Alliance</div>
  <div class="pageno">5</div>
  <p class="abs th-intro">Sed ut perspiciatis unde omnis iste natus error sit volup tatem accus antium dolor emque lauda nt ium, totam rem aperiam, eaque ipsa quae ab illo.</p>
  <ul class="abs th-list">
    <li><svg width="6" height="5" viewBox="0 0 6 5"><path d="M.5 2.5l1.7 1.7L5.5.6" stroke="var(--green)" fill="none"/></svg>Sed ut perspiciatis unde omnis iste natus error</li>
    <li><svg width="6" height="5" viewBox="0 0 6 5"><path d="M.5 2.5l1.7 1.7L5.5.6" stroke="var(--green)" fill="none"/></svg>sit volup tatem accus antium dolor emque lauda</li>
    <li><svg width="6" height="5" viewBox="0 0 6 5"><path d="M.5 2.5l1.7 1.7L5.5.6" stroke="var(--green)" fill="none"/></svg>totam rem aperiam, eaque ipsa quae ab illo</li>
    <li><svg width="6" height="5" viewBox="0 0 6 5"><path d="M.5 2.5l1.7 1.7L5.5.6" stroke="var(--green)" fill="none"/></svg>inventore very tatis et quasi architecto beatae.</li>
  </ul>
  <div class="abs th-box">We are a famous <b>DIGITAL COMPANY</b> in United States specialized in Web, Mobile Design/ Development, Mobile Apps and Social Media Marketing .</div>
</section>

<!-- 6 statistic heavy -->
<section class="slide c3 r2">
  <div class="photo abs st-photo" role="img" aria-label="Faded office workers reviewing documents"></div>
  <div class="title" style="left:28px">Statistic <em>Heavy</em></div>
  <svg class="abs" style="left:71px;top:60px;width:14px;height:12px" viewBox="0 0 14 12"><path d="M1 11h12M3 10V7M6 10V5M9 10V3M12 10V1" stroke="#889" fill="none"/></svg>
  <svg class="abs" style="left:152px;top:60px;width:14px;height:12px" viewBox="0 0 14 12"><circle cx="7" cy="4" r="2.6" stroke="#889" fill="none"/><path d="M2 11c0-3 2.2-4.5 5-4.5S12 8 12 11z" stroke="#889" fill="none"/></svg>
  <svg class="abs" style="left:233px;top:60px;width:14px;height:12px" viewBox="0 0 14 12"><path d="M7 11L2 6a2.8 2.8 0 015-3.5A2.8 2.8 0 0112 6z" stroke="#889" fill="none"/></svg>
  <svg class="abs" style="left:314px;top:60px;width:14px;height:12px" viewBox="0 0 14 12"><path d="M2 7l5-5h5v5l-5 5z" stroke="#889" fill="none"/><circle cx="10" cy="4" r=".8" fill="#889"/></svg>
  <div class="abs stat" style="left:33px"><div style="height:12px"></div><div class="stat-num">9,523</div><div class="stat-lab">Vivamus vel.</div></div>
  <div class="abs stat" style="left:114px"><div style="height:12px"></div><div class="stat-num">192,506</div><div class="stat-lab">Massa lectus.</div></div>
  <div class="abs stat" style="left:195px"><div style="height:12px"></div><div class="stat-num">7,8/5</div><div class="stat-lab">Nunc quam libero.</div></div>
  <div class="abs stat" style="left:276px"><div style="height:12px"></div><div class="stat-num">867.599</div><div class="stat-lab">Feugiat ut ante.</div></div>
  <div class="abs stat-sep" style="left:118px"></div>
  <div class="abs stat-sep" style="left:198px"></div>
  <div class="abs stat-sep" style="left:281px"></div>
  <div class="abs st-band"></div>
  <div class="abs st-head">PRAESENT MALESUADA TEMPUS</div>
  <p class="abs st-text">Praesent malesuada tempus sapien in consectetur. Nullam eu lobortis nisl. Etiam placerat quis dui non varius. Donec dapibus mi eu eros dictum, congue tempus metus sagittis.</p>
  <div class="abs url-pill">www.brighttowns-example.org</div>
</section>

<!-- 7 world map -->
<section class="slide c1 r3">
  <div class="stripe"></div>
  <div class="title">World <em>Map</em></div>
  <div class="brand">Bright Towns Alliance</div>
  <div class="pageno">7</div>
  <div class="abs map" role="img" aria-label="World map with the Americas in blue, Africa in orange, Europe and Asia in grey"></div>
  <div class="abs map-rule"></div>
  <div class="abs region" style="left:265px;top:56px"><div class="pct">15%</div><div class="name">Europe</div><div class="desc">The quick, brown fox jumps over a lazy dog.</div></div>
  <div class="abs region" style="left:335px;top:56px"><div class="pct">30%</div><div class="name">North America</div><div class="desc">The quick, brown fox jumps over a lazy dog.</div></div>
  <div class="abs region" style="left:265px;top:126px"><div class="pct">20%</div><div class="name">Africa</div><div class="desc">The quick, brown fox jumps over a lazy dog.</div></div>
  <div class="abs region" style="left:335px;top:126px"><div class="pct">35%</div><div class="name">Asia</div><div class="desc">The quick, brown fox jumps over a lazy dog.</div></div>
</section>

<!-- 8 multi column table -->
<section class="slide c2 r3">
  <div class="stripe"></div>
  <div class="title">Multi Column <em>Table</em></div>
  <div class="brand">Bright Towns Alliance</div>
  <div class="pageno">8</div>
  <svg class="abs tb-ico" style="left:34px;top:62px" viewBox="0 0 30 30"><circle cx="15" cy="15" r="14" fill="none" stroke="var(--navy)" stroke-width="1.3"/><path d="M9 9l12 12M21 9L9 21" stroke="var(--navy)" stroke-width="2"/></svg>
  <svg class="abs tb-ico" style="left:80px;top:62px" viewBox="0 0 30 30"><circle cx="15" cy="15" r="14" fill="none" stroke="var(--navy)" stroke-width="1.3"/><path d="M15 11v11" stroke="var(--navy)" stroke-width="2.2"/><path d="M12 7v3a3 3 0 006 0V7" stroke="var(--navy)" stroke-width="1.5" fill="none"/></svg>
  <div class="abs tb-head">Company budget files 2017</div>
  <p class="abs tb-lead">Lorem ipsum dolor sit amet, ligula suspendisse nulla pretium, rhoncus tempor fermentum, enim integer ad vestibulum volutpat. Nisl rhoncus turpis est, vel elit, congue wisi enim nunc ultricies sit, magna tincidunt.</p>
  <table class="abs grid">
    <thead><tr><th style="width:86px">Nisl rhoncus turpis est</th><th>2014</th><th>2015</th><th>2016</th><th>2017</th></tr></thead>
    <tbody>
      <tr><td>Praesent condimentum arcu</td><td>4.456</td><td>4.456</td><td>4.456</td><td>4.456</td></tr>
      <tr><td>Praesent condimentum arcu</td><td>5.345</td><td>5.345</td><td>5.345</td><td>5.345</td></tr>
      <tr><td>Praesent condimentum arcu</td><td>6.567</td><td>6.567</td><td>6.567</td><td>6.567</td></tr>
      <tr><td>Praesent condimentum arcu</td><td>7.678</td><td>7.678</td><td>7.678</td><td>7.678</td></tr>
      <tr><td>Praesent condimentum arcu</td><td>8.789</td><td>8.789</td><td>8.789</td><td>8.789</td></tr>
    </tbody>
    <tfoot><tr><td>CHANGE 20%</td><td></td><td></td><td></td><td></td></tr></tfoot>
  </table>
  <div class="abs mgr">
    <div class="mgr-head">STATS MANAGER</div>
    <div class="mgr-cell">THIS YEAR<b>17,250</b></div>
    <div class="mgr-cell">THIS MONTH<b>3,000</b></div>
    <div class="mgr-cell">THIS WEEK<b>450</b></div>
    <div class="mgr-cell">TODAY<b>225</b></div>
  </div>
</section>

<!-- 9 two pictures -->
<section class="slide c3 r3">
  <div class="stripe"></div>
  <div class="title">Two <em>Pictures</em></div>
  <div class="brand">Bright Towns Alliance</div>
  <div class="pageno">9</div>
  <div class="photo abs tp-left" role="img" aria-label="City skyline in warm evening light"></div>
  <div class="abs tp-mid"></div>
  <div class="photo abs tp-right" role="img" aria-label="Downtown towers seen from above at sunset"></div>
  <div class="abs tp-head">HEADING TEXT</div>
  <p class="abs tp-text">Lorem ipsum dolor sit amet, consec tetur adip iscing elit, sed do eiusmod tempor consec tetur adip iscing elit.</p>
  <div class="btn" style="left:176px;top:117px;width:78px;height:11px">Visit Us</div>
  <div class="abs" style="left:168px;top:116px;width:16px;height:13px;background:var(--navy);border-radius:6px"></div>
  <svg class="abs" style="left:171px;top:118px;width:9px;height:9px" viewBox="0 0 10 10"><circle cx="5" cy="5" r="4" fill="none" stroke="#fff" stroke-width=".8"/><path d="M1 5h8M5 1c-2 2.5-2 5.5 0 8M5 1c2 2.5 2 5.5 0 8" stroke="#fff" stroke-width=".6" fill="none"/></svg>
  <p class="abs tp-body">Lorem ipsum dolor sit amet, consec tetur adip iscing elit, sed do eiusmod tempor consec tetur adip iscing elit, sed do eiusmod tempor consec tetur adip iscing elit, sed do eiusmod tempor consec tetur adip iscing elit, sed do eiusmod tempor consec consec tetur adip iscing elit, sed do eiusmod tempor consec</p>
</section>

<!-- 10 monthly timeline -->
<section class="slide c1 r4">
  <div class="stripe"></div>
  <div class="title">Monthly <em>Timeline</em></div>
  <div class="brand">Bright Towns Alliance</div>
  <div class="pageno">10</div>
  <svg class="abs" style="left:0;top:0;width:392px;height:220px" viewBox="0 0 392 220">
    <line x1="40" y1="125" x2="352" y2="125" stroke="#444" stroke-width="1"/>
    <g fill="#444">
      <circle cx="40" cy="125" r="2.6"/><circle cx="68" cy="125" r="2.6"/><circle cx="96" cy="125" r="2.6"/><circle cx="124" cy="125" r="2.6"/>
      <circle cx="152" cy="125" r="2.6"/><circle cx="180" cy="125" r="2.6"/><circle cx="208" cy="125" r="2.6"/><circle cx="236" cy="125" r="2.6"/>
      <circle cx="264" cy="125" r="2.6"/><circle cx="292" cy="125" r="2.6"/><circle cx="320" cy="125" r="2.6"/><circle cx="352" cy="125" r="2.6"/>
    </g>
    <g stroke="#ccc" stroke-width=".6">
      <line x1="40" y1="60" x2="40" y2="122"/><line x1="152" y1="75" x2="152" y2="122"/><line x1="320" y1="60" x2="320" y2="122"/>
      <line x1="124" y1="128" x2="124" y2="180"/><line x1="236" y1="128" x2="236" y2="190"/>
    </g>
    <circle cx="40" cy="57" r="9" fill="var(--sky)"/><path d="M40 52a3 3 0 012.5 4.7L42 59h-4l-.5-2.3A3 3 0 0140 52z" fill="#fff"/>
    <circle cx="152" cy="72" r="9" fill="var(--green)"/><circle cx="152" cy="72" r="3.5" fill="none" stroke="#fff" stroke-width="1.2"/>
    <circle cx="320" cy="57" r="9" fill="var(--navy)"/><rect x="315" y="55" width="10" height="6" fill="#fff"/><rect x="318" y="53" width="4" height="2" fill="none" stroke="#fff" stroke-width=".8"/>
    <circle cx="124" cy="183" r="9" fill="var(--orange)"/><rect x="119" y="179" width="10" height="8" fill="none" stroke="#fff" stroke-width="1"/>
    <circle cx="236" cy="193" r="9" fill="var(--purple)"/><path d="M231 196l8-8 2 2-8 8h-2z" fill="#fff"/>
  </svg>
  <div class="abs tl-text" style="left:53px;top:50px"><b>Lorem Ipsum is simply dummy text</b> of the printing</div>
  <div class="abs tl-text" style="left:165px;top:64px"><b>Lorem Ipsum is simply dummy text</b> of the printing</div>
  <div class="abs tl-text" style="left:256px;top:50px;text-align:right"><b>Lorem Ipsum is simply dummy text</b> of the printing</div>
  <div class="abs tl-text" style="left:138px;top:176px"><b>Lorem Ipsum is simply dummy text</b> of the printing</div>
  <div class="abs tl-text" style="left:250px;top:186px"><b>Lorem Ipsum is simply dummy text</b> of the printing</div>
  <div class="abs tl-month" style="left:59px;top:112px">February</div>
  <div class="abs tl-month" style="left:119px;top:112px">April</div>
  <div class="abs tl-month" style="left:173px;top:111px">June</div>
  <div class="abs tl-month" style="left:228px;top:112px">August</div>
  <div class="abs tl-month" style="left:284px;top:112px">October</div>
  <div class="abs tl-month" style="left:336px;top:112px;color:var(--navy);font-weight:700">December</div>
  <div class="abs tl-year" style="left:343px;top:104px">2017</div>
  <div class="abs tl-month" style="left:31px;top:131px;color:var(--navy);font-weight:700">January</div>
  <div class="abs tl-year" style="left:34px;top:138px">2017</div>
  <div class="abs tl-month" style="left:89px;top:131px">March</div>
  <div class="abs tl-month" style="left:146px;top:131px">May</div>
  <div class="abs tl-month" style="left:203px;top:131px">July</div>
  <div class="abs tl-month" style="left:254px;top:131px">September</div>
  <div class="abs tl-month" style="left:309px;top:131px">November</div>
</section>

<!-- 11 linear process -->
<section class="slide c2 r4">
  <div class="stripe"></div>
  <div class="title">Linear <em>Process</em></div>
  <div class="brand">Bright Towns Alliance</div>
  <div class="pageno">11</div>
  <svg class="abs" style="left:0;top:0;width:392px;height:220px" viewBox="0 0 392 220" font-family="Open Sans, sans-serif" font-size="5.4" fill="#fff" text-anchor="middle">
    <path d="M24 112h60l7 8-7 8H24z" fill="var(--navy)"/>
    <path d="M84 112h57l7 8-7 8H84l7-8z" fill="var(--sky)"/>
    <path d="M141 112h57l7 8-7 8h-57l7-8z" fill="var(--green)"/>
    <path d="M198 112h57l7 8-7 8h-57l7-8z" fill="var(--orange)"/>
    <path d="M255 112h57l7 8-7 8h-57l7-8z" fill="var(--red)"/>
    <path d="M312 112h57l7 8-7 8h-57l7-8z" fill="var(--purple)"/>
    <text x="57" y="122">EXECUTE</text><text x="117" y="122">REVIEW</text><text x="174" y="122">INDICATE</text>
    <text x="231" y="122">IDENTIFY</text><text x="288" y="122">CHECKING</text><text x="344" y="122">CONFIRM</text>
    <g stroke="#bbb" stroke-width=".6"><line x1="84" y1="50" x2="84" y2="110"/><line x1="198" y1="50" x2="198" y2="110"/><line x1="312" y1="50" x2="312" y2="110"/>
      <line x1="24" y1="130" x2="24" y2="180"/><line x1="141" y1="130" x2="141" y2="180"/><line x1="255" y1="130" x2="255" y2="180"/></g>
    <g fill="none" stroke="#888" stroke-width=".8">
      <rect x="88" y="53" width="12" height="14"/><path d="M90 57h8M90 60h8M90 63h6"/>
      <circle cx="208" cy="58" r="4.5"/><path d="M205 61l-4 4"/>
      <path d="M318 67v-8h3l3-6c2 0 2 2 1.5 4H330v4l-2 6z"/>
      <circle cx="34" cy="142" r="5"/><circle cx="34" cy="142" r="2"/>
      <path d="M148 148l8-10 3 2-8 10-4 1z"/>
      <path d="M262 134h14v9h-8l-4 3v-3h-2z"/>
    </g>
  </svg>
  <div class="abs pr-note" style="left:86px;top:77px">Vestibulum lobortis, libero vel gravida pretium.</div>
  <div class="abs pr-note" style="left:200px;top:77px">Vestibulum lobortis, libero vel gravida pretium.</div>
  <div class="abs pr-note" style="left:314px;top:77px">Vestibulum lobortis, libero vel gravida pretium.</div>
  <div class="abs pr-note" style="left:26px;top:157px">Vestibulum lobortis, libero vel gravida pretium.</div>
  <div class="abs pr-note" style="left:143px;top:157px">Vestibulum lobortis, libero vel gravida pretium.</div>
  <div class="abs pr-note" style="left:257px;top:157px">Vestibulum lobortis, libero vel gravida pretium.</div>
</section>

<!-- 12 thank you -->
<section class="slide c3 r4">
  <div class="photo abs ty-photo" role="img" aria-label="Aerial city view with a deep blue overlay"></div>
  <div class="stripe" style="width:10px"></div>
  <div class="abs ty-head">THANK <em>YOU</em></div>
  <p class="abs ty-text">Praesent malesuada tempus sapien in consectetur. Nullam eu lobortis nisl. Etiam placerat quis dui non varius. Donec dapibus mi eu eros dictum, congue tempus metus sagittis.</p>
  <svg class="abs" style="left:160px;top:118px;width:110px;height:9px" viewBox="0 0 110 9">
    <circle cx="6" cy="4.5" r="4" fill="var(--sky)"/><circle cx="55" cy="4.5" r="4" fill="var(--orange)"/><circle cx="104" cy="4.5" r="4" fill="var(--green)"/>
  </svg>
  <div class="abs ty-contact" style="left:136px">info@brighttowns-example.org</div>
  <div class="abs ty-contact" style="left:185px">1-555-0148</div>
  <div class="abs ty-contact" style="left:234px">www.brighttowns-example.net</div>
  <div class="abs ty-pill">Bright Towns Alliance</div>
</section>

</div>
</body>
</html>
```